Billboard design - consider what a billboard is

Design a billboard using my logo - Billboard is 6m x 3m
A Billboard is advertising for my company that is on a big sign.

Has to be clean and easy to read, and ideally highlights that we are Residential and Commercial builders.

Keep it clean and easy to read

The contact number for the board is

022 583 7092
www.harbourframeworks.co.nz
info@harbourframeworks.co.nz

Doesnt have to have all contact details if it doesnt fit

Has to catch peoples attention to contact us if they need a builder

Can you please change the sign to be all white writing, with black background ?
Updates

Please consider what a billboard is...

The design needs to be suitable for a billboard..

Target Market(s)

people driving past

Industry/Entity Type

Construction

Logo Text

Wellington Builder, website email address, contact number

Colors
0054AA
0677BA
7BADD7
CADEEF
E8F1F8

Requirements
Must have
• Easy to read
Nice to have
• easy to read, can clearly see contact details

```html
<!DOCTYPE html>
<html lang="en">
<head>
<meta charset="utf-8">
<title>Harbour Frameworks Billboard</title>
<link rel="stylesheet" href="https://fonts.googleapis.com/css2?family=Arimo:wght@700&display=swap">
<style>
  :root {
    --board: #000000;
    --ink: #ffffff;
    --accent: #0677ba;
    --frame: #8a8280;
    --sky: #7bb0e0;
    --sky-light: #cadeef;
    --brick: #d9825a;
    --khaki: #c9a877;
  }
  * { margin: 0; padding: 0; box-sizing: border-box; }
  html, body { width: 1200px; height: 600px; overflow: hidden; background: var(--board); }
  .billboard {
    position: relative;
    width: 1200px;
    height: 600px;
    background: var(--board);
    font-family: "Arimo", Arial, sans-serif;
    font-weight: 700;
    color: var(--ink);
  }
  .hero-panel {
    position: absolute;
    left: 0;
    top: 0;
    width: 1200px;
    height: 600px;
  }
  .brand-name {
    position: absolute;
    left: 28px;
    top: 34px;
    font-size: 104px;
    line-height: 1.06;
    letter-spacing: -1px;
    color: var(--ink);
  }
  .tagline-rule {
    position: absolute;
    left: 32px;
    top: 300px;
    width: 600px;
    height: 5px;
    background: var(--accent);
  }
  .tagline {
    position: absolute;
    left: 32px;
    top: 318px;
    width: 600px;
    font-size: 27px;
    line-height: 1;
    letter-spacing: 1px;
    text-transform: uppercase;
    color: var(--ink);
    white-space: nowrap;
  }
  .contact-list {
    position: absolute;
    left: 28px;
    top: 428px;
    list-style: none;
  }
  .contact-item {
    display: flex;
    align-items: center;
    height: 42px;
    margin-bottom: 14px;
  }
  .contact-icon { width: 42px; height: 42px; flex: none; }
  .contact-text {
    margin-left: 20px;
    font-size: 30px;
    line-height: 1;
    color: var(--ink);
    white-space: nowrap;
  }
</style>
</head>
<body>
<main class="billboard">
  <svg class="hero-panel" viewBox="0 0 1200 600">
    <defs>
      <linearGradient id="site-tones" x1="0" y1="0" x2="0" y2="1">
        <stop offset="0" stop-color="var(--sky)"/>
        <stop offset="0.35" stop-color="var(--sky-light)"/>
        <stop offset="0.6" stop-color="var(--brick)"/>
        <stop offset="1" stop-color="var(--khaki)"/>
      </linearGradient>
    </defs>
    <path role="img" aria-label="Photo of two builders in white hard hats talking on a brick construction site with a crane under blue sky"
          d="M978 0 L1200 0 L1200 600 L792 600 L690 275 Q676 225 712 193 Z"
          fill="url(#site-tones)"/>
    <path d="M978 0 L712 193 Q676 225 690 275 L792 600"
          fill="none" stroke="var(--frame)" stroke-width="5" stroke-linejoin="round"/>
  </svg>

  <h1 class="brand-name">Harbour<br>Frameworks</h1>
  <div class="tagline-rule"></div>
  <p class="tagline">Residential &amp; Commercial Builders</p>

  <ul class="contact-list">
    <li class="contact-item">
      <svg class="contact-icon" viewBox="0 0 42 42" aria-hidden="true">
        <circle cx="21" cy="21" r="19.5" fill="none" stroke="var(--ink)" stroke-width="2"/>
        <path d="M14 12 l4 -1 l3 6 l-3 2 q2 5 6 7 l2 -3 l6 3 l-1 4 q-2 2 -6 1 q-10 -4 -13 -14 q0 -4 2 -5 z" fill="var(--ink)"/>
      </svg>
      <span class="contact-text">022 583 7092</span>
    </li>
    <li class="contact-item">
      <svg class="contact-icon" viewBox="0 0 42 42" aria-hidden="true">
        <g fill="none" stroke="var(--ink)" stroke-width="2">
          <circle cx="21" cy="21" r="19.5"/>
          <ellipse cx="21" cy="21" rx="8" ry="19.5"/>
          <line x1="21" y1="1.5" x2="21" y2="40.5"/>
          <line x1="1.5" y1="21" x2="40.5" y2="21"/>
          <path d="M5 11 h32 M5 31 h32"/>
        </g>
      </svg>
      <span class="contact-text">www.harbourframeworks.co.nz</span>
    </li>
    <li class="contact-item">
      <svg class="contact-icon" viewBox="0 0 42 42" aria-hidden="true">
        <g fill="none" stroke="var(--ink)" stroke-width="2.5" stroke-linejoin="round">
          <rect x="2" y="3" width="38" height="36" rx="2"/>
          <path d="M2 5 L21 24 L40 5 M2 37 L16 20 M40 37 L26 20"/>
        </g>
      </svg>
      <span class="contact-text">info@harbourframeworks.co.nz</span>
    </li>
  </ul>
</main>
</body>
</html>
```